Jewelry Shop Needs a Business Card Design

***We want a very sharp and unforgettable pantone for the Business Card. ***
***We do not want the business card or logo only in black, white and grey color!!!Please provide us a main color as our brand topic! Thanks!! ***

Mabel’s Nook is a Hong Kong based fine jewelry brand.

We want a very nice, simple and elegant business card design for Mabel's Nook Brand. The company's logo has been uploaded already.

You can design with below info:

Dorian Fung
Director
M: +852 94273658
T: +852 35820417
F: +852 35820419
E: dorian.fung@mabelsnook.example
5/F , Harbourlight Tower, 12-18 Orchid Lane, Wan Tung Kok, Kowloon, Hong Kong

Target Market(s)

Mabel’s Nook philosophy is a jewelry icon of young, creative, trendy, fashionable, stylish, energetic, and elegant. For Mabel’s Nook, jewelry is one collection of artworks, the most important items in personal life.

Industry/Entity Type

Jewelry

Requirements
Must have
• We want a very sharp and unforgettable pantone for the Business Card.

```html
<!DOCTYPE html>
<html lang="en">
<head>
<meta charset="utf-8">
<title>Mabel’s Nook — Business Card</title>
<link rel="stylesheet" href="https://fonts.googleapis.com/css2?family=Cinzel:wght@600&family=Crimson+Text:wght@400&display=swap">
<style>
  :root {
    --page: #ffffff;
    --ink: #141414;
    --rose-edge: #d2386c;
    --rose-mid: #e45f73;
    --salmon-glow: #ef8f6c;
  }
  html, body {
    margin: 0;
    padding: 0;
    width: 1200px;
    height: 381px;
    overflow: hidden;
    background: var(--page);
  }
  .canvas {
    position: relative;
    width: 1200px;
    height: 381px;
  }
  .card {
    position: absolute;
    top: 20px;
    width: 573px;
    height: 327px;
    overflow: hidden;
  }
  .card--front { left: 16px; }
  .card--back { left: 614px; }
  .card__texture {
    position: absolute;
    inset: 0;
    background:
      radial-gradient(ellipse 60% 70% at 48% 45%, var(--salmon-glow) 0%, rgba(239,143,108,0) 70%),
      radial-gradient(ellipse 90% 100% at 50% 50%, var(--rose-mid) 0%, var(--rose-edge) 100%);
  }
  .brand-mark {
    position: absolute;
    display: block;
  }
  .brand-mark circle { fill: var(--ink); }
  .brand-name {
    position: absolute;
    margin: 0;
    font-family: "Cinzel", "Times New Roman", serif;
    font-weight: 600;
    color: var(--ink);
    letter-spacing: 0.06em;
    white-space: nowrap;
    transform: translateX(-50%);
  }
  .card--front .brand-mark { left: 227px; top: 98px; width: 120px; height: 120px; }
  .card--front .brand-name { left: 287px; top: 230px; font-size: 21px; }
  .card--back .brand-mark { left: 102px; top: 98px; width: 102px; height: 102px; }
  .card--back .brand-name { left: 153px; top: 222px; font-size: 18px; }
  .contact {
    position: absolute;
    left: 322px;
    top: 56px;
    font-family: "Crimson Text", "Times New Roman", serif;
    color: var(--ink);
  }
  .contact__name {
    margin: 0;
    font-size: 22px;
    font-weight: 400;
    line-height: 1.1;
  }
  .contact__role {
    margin: 2px 0 0;
    font-size: 14px;
    line-height: 1.2;
  }
  .contact__details {
    margin: 20px 0 0;
    font-size: 14.5px;
    line-height: 20.5px;
    font-style: normal;
    white-space: nowrap;
  }
</style>
</head>
<body>
<main class="canvas">
  <section class="card card--front">
    <div class="card__texture" role="img" aria-label="Mottled rose and coral painted texture"></div>
    <svg class="brand-mark" viewBox="0 0 100 100" aria-hidden="true"><circle cx="50" cy="50" r="50"/></svg>
    <p class="brand-name">Mabel’s Nook</p>
  </section>

  <section class="card card--back">
    <div class="card__texture" role="img" aria-label="Mottled rose and coral painted texture"></div>
    <svg class="brand-mark" viewBox="0 0 100 100" aria-hidden="true"><circle cx="50" cy="50" r="50"/></svg>
    <p class="brand-name">Mabel’s Nook</p>
    <div class="contact">
      <h1 class="contact__name">Dorian Fung</h1>
      <p class="contact__role">Director</p>
      <address class="contact__details">
        M: +852 94273658<br>
        T: +852 35820417<br>
        F: +852 35820419<br>
        E: dorian.fung@mabelsnook.example<br>
        5/F , Harbourlight Tower, 12-18<br>
        Orchid Lane, Wan Tung Kok,<br>
        Kowloon, Hong Kong
      </address>
    </div>
  </section>
</main>
</body>
</html>
```